Corvana Wound Care Business card design

We need a business card designed around our logo which was provided. The logo of preference is the colored. Also the colors and fonts were provided.

Target Market(s)

Our Referral partners are home health agencies.

Industry/Entity Type

Healthcare

Contact Information for Business Card

Name , Phone #, Email , Title

Requirements
Nice to have
• Creativity
Should not have
• basic

```html
<!DOCTYPE html>
<html lang="en">
<head>
<meta charset="utf-8">
<title>Corvana Wound Care – Business Card</title>
<link rel="stylesheet" href="https://fonts.googleapis.com/css2?family=Montserrat:wght@500;600;700&display=swap">
<style>
  :root {
    --backdrop: #2c2c2e;
    --card-white: #f7f7f5;
    --brand-navy: #0d3a94;
    --brand-blue: #1450b4;
    --brand-sky: #0ea0e0;
    --on-navy: #ffffff;
  }
  * { box-sizing: border-box; margin: 0; padding: 0; }
  html, body {
    width: 1200px; height: 800px; overflow: hidden;
    background: var(--backdrop);
    font-family: "Montserrat", Arial, sans-serif;
  }
  .canvas {
    position: relative; width: 1200px; height: 800px;
    display: flex; align-items: center; justify-content: center; gap: 60px;
  }
  .card {
    position: relative; width: 520px; height: 298px;
    border-radius: 3px; box-shadow: 0 18px 40px rgba(0,0,0,.45);
    overflow: hidden;
  }
  .card--front { background: var(--card-white); color: var(--brand-navy); }
  .card--back {
    background: var(--brand-navy); color: var(--on-navy);
    display: flex; align-items: center; justify-content: center;
  }
  .corner-accent {
    position: absolute; left: -24px; top: -20px;
    width: 190px; height: 150px; border-radius: 0 0 28px 0;
    background: linear-gradient(135deg, var(--brand-navy) 0%, var(--brand-blue) 45%, var(--brand-sky) 100%);
  }
  .holder {
    position: absolute; left: 150px; top: 74px; width: 240px; text-align: center;
  }
  .holder__name { font-size: 30px; font-weight: 700; letter-spacing: .2px; line-height: 1.05; }
  .holder__title { font-size: 15px; font-weight: 600; margin-top: 3px; }
  .contact {
    position: absolute; left: 318px; top: 176px;
    list-style: none; font-size: 13px; font-weight: 500;
  }
  .contact__item { display: flex; align-items: center; gap: 7px; margin-bottom: 10px; white-space: nowrap; }
  .contact__icon { width: 18px; height: 18px; flex: none; }
  .wordmark {
    display: flex; align-items: center; gap: 10px;
    font-weight: 700; white-space: nowrap;
  }
  .wordmark__dot { border-radius: 50%; background: currentColor; flex: none; }
  .card--front .wordmark { position: absolute; left: 44px; bottom: 42px; color: var(--brand-navy); font-size: 18px; }
  .card--front .wordmark__dot { width: 12px; height: 12px; }
  .card--back .wordmark { color: var(--on-navy); font-size: 26px; }
  .card--back .wordmark__dot { width: 18px; height: 18px; }
</style>
</head>
<body>
<main class="canvas">
  <section class="card card--front" aria-label="Business card front">
    <div class="corner-accent" role="img" aria-label="Blue gradient brand decoration"></div>
    <div class="holder">
      <p class="holder__name">Yourname</p>
      <p class="holder__title">Director</p>
    </div>
    <ul class="contact">
      <li class="contact__item">
        <svg class="contact__icon" viewBox="0 0 20 20" aria-hidden="true">
          <circle cx="10" cy="10" r="9" fill="none" stroke="currentColor" stroke-width="1.4"/>
          <path d="M7 5.5l1.6 1.6-1 1.2c.7 1.5 1.6 2.4 3.1 3.1l1.2-1 1.6 1.6-1 1.4c-3 0-6.2-3.2-6.2-6.2z" fill="currentColor"/>
        </svg>
        555.201.0148
      </li>
      <li class="contact__item">
        <svg class="contact__icon" viewBox="0 0 20 20" aria-hidden="true">
          <circle cx="10" cy="10" r="9" fill="none" stroke="currentColor" stroke-width="1.4"/>
          <rect x="5.5" y="6.8" width="9" height="6.4" rx=".8" fill="currentColor"/>
          <path d="M5.8 7.2l4.2 3.2 4.2-3.2" fill="none" stroke="var(--card-white)" stroke-width="1"/>
        </svg>
        hello@corvanacare.com
      </li>
    </ul>
    <div class="wordmark"><span class="wordmark__dot"></span>Corvana Wound Care</div>
  </section>

  <section class="card card--back" aria-label="Business card back">
    <div class="wordmark"><span class="wordmark__dot"></span>Corvana Wound Care</div>
  </section>
</main>
</body>
</html>
```